Rack Card for Portuguese Walking Food Tour

I would like a vertical rack card measuring 99x210mm. Here is the information I would like to include. It does not need to be in this format. We are located in Setubal, Portugal.
Please use the attached Teal Heron Logo.
Setúbal: Tradition and Today
Experience the culinary delights of Setúbal, Portugal with a walking food tour around our waterfront village. Discover the Mercado da Gaivota Branca, voted one of the world’s best markets by Metro Ledger, and indulge in local wines and dishes. Prepare for a calm stroll on flat streets. No hills to climb on this tour.
Duration: 4 hours
www.brinebasketwalks.com
+351 265 000 487

```html
<!DOCTYPE html>
<html lang="en">
<head>
<meta charset="utf-8">
<title>Setúbal Rack Card – Teal Heron Tours</title>
<link rel="stylesheet" href="https://fonts.googleapis.com/css2?family=Outfit:wght@400;500;600;700&family=Pacifico&display=swap">
<style>
  :root {
    --orange: #e06c38;
    --white: #ffffff;
    --page: #ffffff;
    --market-top: linear-gradient(160deg, #c9ccd0 0%, #7d8a86 35%, #b5743f 60%, #6a7a4a 100%);
    --fish: linear-gradient(165deg, #c9d3d8 0%, #d8876a 25%, #c85e48 55%, #e0a48e 80%, #9a4a3c 100%);
    --market-bottom: linear-gradient(150deg, #a8adb0 0%, #7b8f52 40%, #c9a03c 70%, #8a6a4a 100%);
  }
  * { box-sizing: border-box; margin: 0; padding: 0; }
  html, body {
    width: 1200px; height: 1064px; overflow: hidden;
    background: var(--page);
    font-family: "Outfit", sans-serif;
  }
  .card {
    position: absolute; top: 104px; width: 425px; height: 897px;
    overflow: hidden;
  }
  .card--front { left: 162px; background: var(--orange); border: 1px solid #222; }
  .card--back { left: 615px; background: var(--orange); }

  .photo { position: absolute; }
  .photo--market-top { left: 0; top: 0; width: 100%; height: 219px; background: var(--market-top); }
  .photo--fish { left: 210px; top: 338px; width: 215px; height: 398px; background: var(--fish); }
  .photo--market-bottom { left: 0; top: 736px; width: 210px; height: 161px; background: var(--market-bottom); }

  .header {
    position: absolute; left: 0; top: 219px; width: 100%; height: 119px;
    text-align: center; color: var(--white);
  }
  .header__title {
    font-family: "Pacifico", cursive; font-weight: 400;
    font-size: 40px; line-height: 1; margin-top: 24px;
  }
  .header__subtitle { font-size: 22px; font-weight: 500; margin-top: 8px; }

  .intro {
    position: absolute; left: 0; top: 338px; width: 210px; height: 398px;
    background: var(--white); color: var(--orange);
    padding: 20px 14px 0 27px;
    font-size: 16px; line-height: 20px; font-weight: 500;
  }
  .intro strong { font-weight: 700; }
  .intro__duration {
    position: absolute; left: 27px; top: 350px;
    display: flex; align-items: center; gap: 6px;
    font-weight: 700;
  }
  .notch { position: absolute; }
  .notch--top { left: 199px; top: 338px; }
  .notch--bottom { left: 199px; top: 726px; }
  .notch--side { left: 209px; top: 627px; }

  .contact {
    position: absolute; left: 210px; top: 736px; width: 215px; height: 161px;
    text-align: center; color: var(--white);
  }
  .brand {
    display: inline-flex; align-items: center; gap: 8px;
    color: var(--white); font-weight: 700;
  }
  .brand__dot { border-radius: 50%; background: var(--white); flex: none; }
  .contact .brand { margin-top: 28px; font-size: 19px; }
  .contact .brand__dot { width: 22px; height: 22px; }
  .contact__details { margin-top: 30px; font-size: 15px; line-height: 20px; font-weight: 500; }

  .card--back .brand {
    position: absolute; left: 50%; top: 448px; transform: translate(-50%, -50%);
    font-size: 30px; white-space: nowrap;
  }
  .card--back .brand__dot { width: 36px; height: 36px; }
</style>
</head>
<body>
  <section class="card card--front">
    <div class="photo photo--market-top" role="img" aria-label="Busy indoor fish and produce market seen from above"></div>

    <header class="header">
      <h1 class="header__title">Setúbal</h1>
      <p class="header__subtitle">Tradition and Today</p>
    </header>

    <div class="intro">
      <p>Experience the culinary delights of <strong>Setúbal, Portugal</strong> with a walking food tour around our waterfront village. Discover the <strong>Mercado da Gaivota Branca</strong>, voted one of the world’s best markets by Metro Ledger, and indulge in local wines and dishes. Prepare for a calm stroll on flat streets. No hills to climb on this tour.</p>
      <p class="intro__duration">
        <svg width="16" height="16" viewBox="0 0 16 16" aria-hidden="true">
          <circle cx="8" cy="8" r="6.5" fill="none" stroke="currentColor" stroke-width="1.8"/>
          <path d="M8 4.5V8.3L10.5 9.8" fill="none" stroke="currentColor" stroke-width="1.8" stroke-linecap="round"/>
        </svg>
        Duration: 4 hours
      </p>
    </div>

    <div class="photo photo--fish" role="img" aria-label="Fresh red mullet on ice at a market stall with a price sign"></div>

    <svg class="notch notch--top" width="22" height="11" viewBox="0 0 22 11" aria-hidden="true"><path d="M0 0H22L11 11Z" fill="var(--orange)"/></svg>
    <svg class="notch notch--bottom" width="22" height="10" viewBox="0 0 22 10" aria-hidden="true"><path d="M0 10H22L11 0Z" fill="var(--orange)"/></svg>
    <svg class="notch notch--side" width="11" height="22" viewBox="0 0 11 22" aria-hidden="true"><path d="M0 0V22L11 11Z" fill="var(--white)"/></svg>

    <div class="photo photo--market-bottom" role="img" aria-label="Market stalls piled with fruit and vegetables"></div>

    <footer class="contact">
      <div class="brand"><span class="brand__dot"></span>Teal Heron Tours</div>
      <p class="contact__details">www.brinebasketwalks.com<br>+351 265 000 487</p>
    </footer>
  </section>

  <section class="card card--back">
    <div class="brand"><span class="brand__dot"></span>Teal Heron Tours</div>
  </section>
</body>
</html>
```